Brighter Than Dawn Home Entertainment

We are a home theater installation company focus on front projection system and home theater surround system. We built highend home theater for people to enjoy movie, sports and gaming on big screen at home.
I'm looking for a dispaly to showcase our work as well as help people build their home theater

Number of Pages Required

3 page

Colors

Designer to choose colors to be used in the design.

Requirements
Must have
• Home Page
• What we do
• Who we are
• Gallery
• Contact Us
Nice to have
• Picture jump out of big screen make a 3D feeling

```html
<!DOCTYPE html>
<html lang="en">
<head>
<meta charset="utf-8">
<title>Brighter Than Dawn Home Entertainment</title>
<link rel="stylesheet" href="https://fonts.googleapis.com/css2?family=Open+Sans:wght@300;400;600;700&display=swap">
<style>
:root{
  --orange:#f26522;
  --dark:#2f3033;
  --darker:#1c1d1f;
  --ink:#3a3a3a;
  --muted:#8a8a8a;
  --white:#ffffff;
  --line:#d6d6d6;
}
*{margin:0;padding:0;box-sizing:border-box}
html,body{width:1200px;height:4255px;overflow:hidden;background:var(--white)}
body{position:relative;font-family:"Open Sans",Arial,sans-serif;color:var(--ink)}
.abs{position:absolute}
.photo{position:absolute}
p{font-size:11px;line-height:1.6}

/* hero */
.hero{left:0;top:0;width:1200px;height:648px;background:radial-gradient(circle at 78% 45%,#6a6a6a 0,#3a3a3a 22%,#1b1b1b 45%,#2a2a2a 70%,#111 100%)}
.nav{left:128px;top:50px;display:flex;gap:26px}
.nav a{color:var(--white);font-size:11px;font-weight:600;text-decoration:none;letter-spacing:.3px}
.nav a.active{border-bottom:2px solid var(--orange);padding-bottom:6px}
.brand{left:1045px;top:24px;display:flex;gap:8px;align-items:flex-start;width:140px}
.brand-mark{width:22px;height:22px;background:var(--orange);flex:none}
.brand-name{color:var(--white);font-size:9px;font-weight:600;line-height:1.25}
.hero-title{left:128px;top:388px;color:var(--white);font-size:30px;font-weight:400;line-height:1.15;width:460px}
.hero-text{left:128px;top:478px;color:#e6e6e6;width:300px;font-size:12px}
.hero-ctrl{left:128px;top:526px;display:flex;gap:40px;align-items:center}
.circles{left:128px;top:636px;display:flex;gap:6px}

/* who we are */
.who{left:332px;top:638px;width:286px;height:582px;background:var(--orange);padding:50px 30px;color:var(--white)}
.who h2{font-size:24px;font-weight:400;margin-bottom:34px}
.who p{color:var(--white);font-weight:600;margin-bottom:28px}
.blows{left:658px;top:988px;width:460px}
.blows h3{font-size:22px;font-weight:400;color:#2b2b2b;line-height:1.2}
.blows p{color:var(--muted);margin-top:14px}
.tweet{left:658px;top:1126px;display:flex;gap:12px;align-items:center;color:#b5b5b5;font-size:11px}
.tweet i{width:14px;height:14px;border-radius:50%;background:#cfcfcf;display:block}
.melb{left:156px;top:1274px;font-size:26px;font-weight:300;color:#2f5673;letter-spacing:.5px}
.col{width:445px}
.col .lead{color:#a8a8a8;font-size:13px;font-weight:300;line-height:1.5;margin-bottom:22px}
.col p{color:#666;margin-bottom:10px}

/* what we do */
.room{left:0;top:1660px;width:1200px;height:610px;background:linear-gradient(160deg,#5b5d60 0,#cfd0cf 30%,#e8e8e6 55%,#3a3b3c 80%,#1d1e1f 100%)}
.what{left:156px;top:1929px;width:346px;height:341px;background:var(--orange);padding:70px 44px;color:var(--white)}
.what h2{font-size:40px;font-weight:400}
.face{left:502px;top:1929px;width:343px;height:341px;background:linear-gradient(135deg,#e9e9e9,#cfcfcf)}
.what-band{left:156px;top:2270px;width:1044px;height:340px;background:var(--orange);padding:76px 44px;display:flex;gap:48px}
.what-band div{width:430px}
.what-band p{color:var(--white);font-weight:600;margin-bottom:16px}

/* gallery */
.gallery{left:156px;top:2610px;width:1044px;height:170px;background:var(--dark)}
.gallery h2{position:absolute;left:50px;top:22px;color:var(--white);font-size:24px;font-weight:400}
.thumbs{position:absolute;left:204px;top:30px;display:flex;gap:5px}
.thumbs span{width:138px;height:100px;display:block;background:linear-gradient(180deg,#c8c8c8,#9d9d9d)}
.bigspeaker{left:156px;top:2780px;width:1044px;height:625px;background:radial-gradient(circle at 48% 45%,#777 0,#2e2e2e 22%,#141414 40%,#9a9a9a 62%,#d4d4dc 80%,#4a4a55 100%)}
.nice{left:156px;top:3225px;width:289px;height:577px;background:var(--orange);padding:40px 34px;color:var(--white)}
.nice h2{font-size:24px;font-weight:400;line-height:1.15;margin-bottom:22px}
.nice p{color:var(--white);font-weight:600;margin-bottom:24px}
.screen{left:445px;top:3225px;width:605px;height:293px;background:linear-gradient(180deg,#c9c9c9,#9a9ea2 60%,#5a6b80)}
.end{left:488px;top:3568px;width:460px}
.end h3{font-size:24px;font-weight:400;color:#2b2b2b;line-height:1.15}
.end p{color:var(--muted);margin-top:12px}
.cable{left:1010px;top:3660px;width:52px;height:142px;background:linear-gradient(90deg,#d5d5d5,#f5f5f5,#bcbcbc)}

/* footer */
.footer{left:0;top:3802px;width:1200px;height:453px;background:var(--dark)}
.fcol{position:absolute;top:56px}
.fcol h4{color:var(--orange);font-size:10px;font-weight:600;margin-bottom:14px}
.fcol li{list-style:none;color:#e8e8e8;font-size:10px;line-height:22px}
.contact{position:absolute;left:845px;top:150px;color:#e8e8e8}
.contact h4{font-size:14px;font-weight:600;margin-bottom:28px}
.crow{display:flex;gap:14px;align-items:flex-start;font-size:13px;line-height:1.5;margin-bottom:18px;color:#cfcfcf}
.signup{position:absolute;left:164px;top:275px;display:flex;gap:18px}
.signup input{height:44px;border:0;background:var(--white);font-family:inherit;font-size:11px;padding:0 14px;color:#666}
.signup button{height:44px;width:110px;border:1px solid #888;background:transparent;color:var(--white);font-family:inherit;font-weight:600;font-size:13px}
.social{position:absolute;left:510px;top:358px;display:flex;gap:14px}
.social i{width:9px;height:9px;border-radius:50%;background:#bdbdbd;display:block}
</style>
</head>
<body>

<section class="photo hero" role="img" aria-label="Close-up of a black loudspeaker driver in a dark room"></section>
<nav class="abs nav">
  <a href="#what" class="active">WHAT WE DO</a>
  <a href="#who">WHO WE ARE</a>
  <a href="#gallery">GALLERY</a>
  <a href="#contact">CONTACT US</a>
</nav>
<div class="abs brand"><span class="brand-mark"></span><span class="brand-name">Brighter Than Dawn Home Entertainment</span></div>
<h1 class="abs hero-title">SPORTS AND GAMING ON BIG SCREEN AT HOME.</h1>
<p class="abs hero-text">Lorem ipsum dolor sit amet, consectetur adipisicing elit, sed do eiusmod tempor incididunt ut labore et dolore</p>
<div class="abs hero-ctrl">
  <svg width="24" height="4"><rect width="24" height="2" fill="#fff"/></svg>
  <svg width="30" height="16" viewBox="0 0 30 16"><path d="M0 8h27M20 1l7 7-7 7" stroke="#fff" stroke-width="1.8" fill="none"/></svg>
</div>
<div class="abs circles">
  <svg width="44" height="44" viewBox="0 0 44 44"><circle cx="22" cy="22" r="20" fill="none" stroke="#fff" stroke-width="2"/><path d="M22 12v19M15 24l7 7 7-7" stroke="#fff" stroke-width="2" fill="none"/></svg>
  <svg width="44" height="44" viewBox="0 0 44 44"><circle cx="22" cy="22" r="20" fill="none" stroke="#f26522" stroke-width="2"/><path d="M12 22h19M24 15l7 7-7 7" stroke="#f26522" stroke-width="2" fill="none"/></svg>
</div>

<section id="who" class="abs who">
  <h2>WHO WE ARE</h2>
  <p>Lorem ipsum dolor sit amet, consectetur adipisicing elit, sed do eiusmod tempor incididunt ut labore et dolore magna aliqua.</p>
  <p>Ut enim ad minim veniam, quis nostrud exercitation ullamco laboris nisi ut aliquip ex ea commodo consequat. Duis aute irure dolor in reprehenderit in voluptate velit esse cillum dolore eu fugiat nulla pariatur.</p>
</section>
<div class="photo" style="left:618px;top:638px;width:582px;height:290px;background:linear-gradient(180deg,#fafafa,#e4e4e4)" role="img" aria-label="Black surround speaker system with subwoofer"></div>
<div class="abs blows">
  <h3>FINALY A LAYOUT THAT BLOWS<br>YOUR HEAD OFF</h3>
  <p>Lorem ipsum dolor sit amet, consectetur adipisicing elit, sed do eiusmod tempor incididunt ut labore et dolore magna aliqua.</p>
</div>
<div class="abs tweet"><i></i><span>Tweet this</span></div>
<div class="photo" style="left:1055px;top:1092px;width:108px;height:270px;background:linear-gradient(90deg,#7f95ad,#c6d3e0,#6c7f95)" role="img" aria-label="Tall blue floor-standing speaker"></div>

<h2 class="abs melb">MELBOURNE, AUSTRALIA</h2>
<div class="abs col" style="left:156px;top:1319px">
  <p class="lead">Lorem ipsum dolor sit amet, consectetur adipisicing elit, sed do eiusmod tempor incididunt ut labore et dolore magna aliqua. Ut enim ad minim veniam, quis nostrud exercitation ullamco laboris nisi ut aliquip ex ea commodo consequat. Duis aute irure dolor in reprehenderit in voluptate velit esse cillum dolore eu fugiat nulla pariatur.</p>
  <p>Excepteur sint occaecat cupidatat non proident, sunt in culpa qui officia deserunt mollit anim id est laborum. Sed ut perspiciatis unde omnis iste natus error sit voluptatem accusantium doloremque laudantium, totam rem aperiam, eaque ipsa quae ab illo inventore veritatis et quasi architecto beatae vitae dicta sunt explicabo. Nemo enim ipsam voluptatem quia voluptas sit aspernatur aut odit aut fugit, sed quia consequuntur magni dolores eos qui ratione voluptatem sequi nesciunt. Neque porro quisquam est, qui dolorem ipsum quia dolor sit amet, consectetur, adipisci velit, sed quia non numquam eius modi tempora incidunt ut labore et dolore magnam aliquam quaerat voluptatem.</p>
</div>
<div class="abs col" style="left:652px;top:1319px">
  <p>Lorem ipsum dolor sit amet, consectetur adipisicing elit, sed do eiusmod tempor incididunt ut labore et dolore magna aliqua. Ut enim ad minim veniam, quis nostrud exercitation ullamco laboris nisi ut aliquip ex ea commodo consequat. Duis aute irure dolor in reprehenderit in voluptate velit esse cillum dolore eu fugiat nulla pariatur.</p>
  <p>Excepteur sint occaecat cupidatat non proident, sunt in culpa qui officia deserunt mollit anim id est laborum. Sed ut perspiciatis unde omnis iste natus error sit voluptatem accusantium doloremque laudantium, totam rem aperiam, eaque ipsa quae ab illo inventore veritatis et quasi architecto beatae vitae dicta sunt explicabo. Nemo enim ipsam voluptatem quia voluptas sit aspernatur aut odit aut fugit, sed quia consequuntur magni dolores eos qui ratione voluptatem sequi nesciunt. Neque porro quisquam est, qui dolorem ipsum quia dolor sit amet, consectetur, adipisci velit, sed quia non numquam eius modi tempora incidunt ut labore et dolore magnam aliquam quaerat voluptatem.</p>
</div>

<div class="photo room" role="img" aria-label="Living room with a wall-mounted television and decor"></div>
<section id="what" class="abs what"><h2>WHAT WE DO</h2></section>
<div class="photo face" role="img" aria-label="Portrait of a surprised man"></div>
<div class="abs what-band">
  <div>
    <p>Lorem ipsum dolor sit amet, consectetur adipisicing elit, sed do eiusmod tempor incididunt ut labore et dolore magna aliqua. Ut enim ad minim veniam, quis nostrud exercitation ullamco laboris nisi ut aliquip ex ea commodo consequat. Duis aute irure dolor in reprehenderit in voluptate velit esse cillum dolore eu fugiat nulla pariatur.</p>
    <p>Excepteur sint occaecat cupidatat non proident, sunt in culpa qui officia deserunt mollit anim id est laborum. Sed ut perspiciatis unde omnis iste natus error sit voluptatem accusantium doloremque laudantium, totam rem aperiam, eaque ipsa quae ab illo inventore veritatis et quasi architecto beatae vitae dicta sunt explicabo. Nemo enim ipsam voluptatem quia voluptas sit aspernatur aut odit.</p>
  </div>
  <div>
    <p>Lorem ipsum dolor sit amet, consectetur adipisicing elit, sed do eiusmod tempor incididunt ut labore et dolore magna aliqua. Ut enim ad minim veniam, quis nostrud exercitation ullamco laboris nisi ut aliquip ex ea commodo consequat. Duis aute irure dolor in reprehenderit in voluptate velit esse cillum dolore eu fugiat nulla pariatur.</p>
    <p>Excepteur sint occaecat cupidatat non proident, sunt in culpa qui officia deserunt mollit anim id est laborum. Sed ut perspiciatis unde omnis iste natus error sit voluptatem.</p>
  </div>
</div>

<section id="gallery" class="abs gallery">
  <h2>GALLERY</h2>
  <div class="thumbs">
    <span role="img" aria-label="Speaker with wooden cabinet"></span>
    <span role="img" aria-label="Black AV receiver"></span>
    <span role="img" aria-label="Home theater speaker set"></span>
    <span role="img" aria-label="Tower speakers and subwoofer"></span>
    <span role="img" aria-label="Surround sound system"></span>
  </div>
</section>
<div class="photo bigspeaker" role="img" aria-label="Close-up of a speaker cone beside carbon fabric"></div>
<section class="abs nice">
  <h2>OHH THIS<br>IS NICE</h2>
  <p>Lorem ipsum dolor sit amet, consectetur adipisicing elit, sed do eiusmod tempor incididunt ut labore et dolore magna aliqua.</p>
  <p>Ut enim ad minim veniam, quis nostrud exercitation ullamco laboris nisi ut aliquip ex ea commodo consequat. Duis aute irure dolor in reprehenderit in voluptate velit esse cillum dolore eu fugiat nulla pariatur.</p>
</section>
<div class="photo screen" role="img" aria-label="Curved projection screen on a round glowing stage"></div>
<div class="abs end">
  <h3>THE END IS NIGH, WELL THE<br>FOOTER ANYWAYS</h3>
  <p>Lorem ipsum dolor sit amet, consectetur adipisicing elit, sed do eiusmod tempor incididunt ut labore et dolore magna aliqua.</p>
</div>
<div class="photo cable" role="img" aria-label="White audio cable with connector"></div>

<footer id="contact" class="abs footer">
  <div class="fcol" style="left:156px"><h4>Quick links</h4><ul><li>A Footer Link</li><li>A Footer Link</li><li>A Footer Link</li><li>A Footer Link</li><li>A Footer Link</li><li>A Footer Link</li><li>A Footer Link</li></ul></div>
  <div class="fcol" style="left:289px"><h4>Our Profile</h4><ul><li>A Footer Link</li><li>A Footer Link</li><li>A Footer Link</li><li>A Footer Link</li><li>A Footer Link</li><li>A Footer Link</li><li>A Footer Link</li></ul></div>
  <div class="fcol" style="left:425px"><h4>Information</h4><ul><li>A Footer Link</li><li>A Footer Link</li><li>A Footer Link</li><li>A Footer Link</li><li>A Footer Link</li></ul></div>
  <div class="fcol" style="left:562px"><h4>Services</h4><ul><li>A Footer Link</li><li>A Footer Link</li><li>A Footer Link</li><li>A Footer Link</li><li>A Footer Link</li><li>A Footer Link</li><li>A Footer Link</li><li>A Footer Link</li></ul></div>
  <div class="fcol" style="left:653px"><h4>Destinations</h4><ul><li>A Footer Link</li><li>A Footer Link</li><li>A Footer Link</li><li>A Footer Link</li><li>A Footer Link</li><li>A Footer Link</li><li>A Footer Link</li></ul></div>
  <div class="contact">
    <h4>Contact</h4>
    <div class="crow">
      <svg width="16" height="20" viewBox="0 0 16 20"><path d="M8 1a6 6 0 0 0-6 6c0 5 6 12 6 12s6-7 6-12a6 6 0 0 0-6-6z" fill="#bdbdbd"/><circle cx="8" cy="7" r="2.3" fill="#2f3033"/></svg>
      <span>Ruko Bintang, Jl. Cahaya Pagi dalem jos<br>No.7 - 8, Kembangan - Jakarta Barat<br>11610 - Indonesia</span>
    </div>
    <div class="crow">
      <svg width="18" height="18" viewBox="0 0 18 18"><path d="M4 1l3 4-2 2c1 2 3 4 5 5l2-2 4 3-2 3C8 16 2 10 1 4z" fill="#bdbdbd"/></svg>
      <span>(+62) 21-5550 1820</span>
    </div>
  </div>
  <form class="signup">
    <input style="width:140px" placeholder="Name">
    <input style="width:130px" placeholder="Contact Phone">
    <input style="width:220px" placeholder="Email">
    <button type="button">Sign Up</button>
  </form>
  <div class="social"><i></i><i></i><i></i><i></i><i></i></div>
</footer>

</body>
</html>
```